Real Estate Agent needs business card design

We have logo designed already, want to have business card designed. Very interested in those smaller size business card as they look very trendy. Business name is called VORENDA REALTY

```html
<!DOCTYPE html>
<html lang="en">
<head>
<meta charset="utf-8">
<title>Vorenda Realty – Business Card</title>
<link rel="stylesheet" href="https://fonts.googleapis.com/css2?family=Noto+Serif:wght@400;700&family=Tinos&display=swap">
<style>
  :root {
    --backdrop: #4a4b4d;
    --card-white: #ffffff;
    --card-gold: #d3aa6e;
    --mark-tan: #e8cfa6;
    --text-gold: #c9a064;
    --text-dark: #2e2216;
    --logo-brown: #6b4a26;
  }
  html, body {
    margin: 0;
    width: 1200px;
    height: 1000px;
    overflow: hidden;
    background: var(--backdrop);
  }
  .sheet {
    position: relative;
    width: 1200px;
    height: 1000px;
    display: flex;
    align-items: center;
    justify-content: center;
    gap: 60px;
  }
  .card {
    position: relative;
    width: 520px;
    height: 408px;
    box-shadow: 0 10px 30px rgba(0,0,0,.35);
    overflow: hidden;
  }
  /* Front: contact side */
  .card--front { background: var(--card-white); }
  .brand-block {
    position: absolute;
    left: 30px;
    top: 50%;
    width: 170px;
    height: 170px;
    margin-top: -85px;
    background: var(--mark-tan);
  }
  .contact {
    position: absolute;
    right: 36px;
    top: 76px;
    text-align: right;
    font-family: "Noto Serif", serif;
    color: var(--text-gold);
    font-size: 19px;
    line-height: 1.3;
  }
  .contact__name {
    font-weight: 700;
    font-size: 20px;
    margin: 0 0 30px;
  }
  .contact__role { margin: 0; }
  .contact__phone { margin: 0 0 30px; }
  .contact__address { margin: 0; font-style: italic; }

  /* Back: brand side */
  .card--back {
    background: var(--card-gold);
    font-family: "Tinos", serif;
    color: var(--text-dark);
    text-align: center;
  }
  .brand {
    position: absolute;
    left: 0;
    right: 0;
    top: 128px;
    display: flex;
    align-items: center;
    justify-content: center;
    gap: 14px;
  }
  .brand__square {
    width: 34px;
    height: 34px;
    background: var(--logo-brown);
  }
  .brand__name {
    font-size: 34px;
    letter-spacing: 2px;
    color: var(--text-dark);
  }
  .website {
    position: absolute;
    left: 0;
    right: 0;
    top: 262px;
    font-size: 19px;
  }
</style>
</head>
<body>
  <main class="sheet">
    <section class="card card--front" aria-label="Business card front">
      <div class="brand-block"></div>
      <div class="contact">
        <p class="contact__name">Elena Marsh</p>
        <p class="contact__role">Senior Property Consultant</p>
        <p class="contact__phone">0400 215 937</p>
        <p class="contact__address">12A, 48 Harbour Street<br>Chatswood, NSW 2067</p>
      </div>
    </section>

    <section class="card card--back" aria-label="Business card back">
      <div class="brand">
        <span class="brand__square"></span>
        <span class="brand__name">VORENDA REALTY</span>
      </div>
      <div class="website">www.vorendarealty.com.au</div>
    </section>
  </main>
</body>
</html>
```